Business Card Design For A Renovation Contractor Company

We need a business card for a new company based in Singapore, our company name is "KT Planora". We are a renovation contractor that builds designs into reality. We build more of F&B restaurants, retail stores and commercial offices. We work very closely with designers. The final design should communicate to our client that we are a company that you can trust, that will plan and complete your project without giving you a headache. I like my client to remember my company as "KT". The beauty of SIMPLE is important.

Industry/Entity Type

Contractor

Requirements
Nice to have
• Black or Red base

```html
<!DOCTYPE html>
<html lang="en">
<head>
<meta charset="utf-8">
<title>KT Planora – Business Card</title>
<link href="https://fonts.googleapis.com/css2?family=Open+Sans:wght@400;600;700;800&display=swap" rel="stylesheet">
<style>
  :root {
    --bg-top: #3a4450;
    --bg-bottom: #454a4f;
    --card-white: #f7f7f7;
    --card-grey: #e4e3e3;
    --card-back: #ededed;
    --brand-red: #e63a26;
    --brand-red-light: #f05a3e;
    --rule-dark: #3b3b3b;
    --ink: #2a2a2a;
    --ink-soft: #555555;
  }
  * { margin: 0; padding: 0; box-sizing: border-box; }
  html, body { width: 1200px; height: 1000px; overflow: hidden; }
  body {
    background: linear-gradient(160deg, var(--bg-top), var(--bg-bottom));
    font-family: "Open Sans", Arial, sans-serif;
    position: relative;
  }
  .card {
    position: absolute;
    left: 320px;
    width: 560px;
    height: 320px;
    overflow: hidden;
    box-shadow: 0 14px 30px rgba(0,0,0,0.45);
  }
  .card--front { top: 150px; background: var(--card-white); }
  .card--back  { top: 530px; background: var(--card-back); }

  .card__panel {
    position: absolute;
    left: 0; right: 0; top: 92px; bottom: 0;
    background: var(--card-grey);
  }
  .card__band {
    position: absolute;
    left: 0; right: 0; bottom: 0;
    height: 42px;
    background: linear-gradient(100deg, var(--brand-red) 0%, var(--brand-red) 40%, var(--brand-red-light) 50%, var(--brand-red) 62%, var(--brand-red) 100%);
    border-top: 7px solid var(--rule-dark);
  }

  .holder { position: absolute; left: 40px; top: 108px; }
  .holder__name {
    color: var(--brand-red);
    font-weight: 800;
    font-size: 22px;
    letter-spacing: 0.5px;
    line-height: 1.2;
  }
  .holder__role { color: var(--ink); font-size: 12px; font-weight: 600; margin-top: 2px; }

  .contact {
    position: absolute;
    left: 60px; top: 178px;
    list-style: none;
    font-size: 10px;
    color: var(--ink-soft);
    line-height: 1.35;
  }
  .contact li { display: flex; gap: 8px; margin-bottom: 4px; }
  .contact svg { width: 10px; height: 10px; flex: none; margin-top: 2px; }

  .brand-box {
    position: absolute;
    right: 24px; top: 20px;
    width: 200px; height: 150px;
    background: #ffffff;
    display: flex; flex-direction: column;
    align-items: center; justify-content: center; gap: 10px;
  }
  .brand-mark {
    width: 46px; height: 46px;
    border-radius: 50%;
    border: 4px solid var(--ink);
  }
  .brand-name {
    font-size: 22px; font-weight: 400;
    color: var(--ink);
    line-height: 1;
  }
  .brand-tagline { font-size: 8px; color: var(--ink-soft); margin-top: -4px; white-space: nowrap; }

  .back-brand {
    position: absolute;
    left: 0; right: 0; top: 58px;
    display: flex; flex-direction: column; align-items: center; gap: 10px;
  }
  .back-brand .brand-mark { width: 62px; height: 62px; border-width: 5px; }
  .back-brand .brand-name { font-size: 34px; }
  .back-brand .brand-tagline {
    font-size: 12px; margin-top: -4px;
    border-top: 1px solid var(--ink);
    padding-top: 1px;
  }
</style>
</head>
<body>

  <section class="card card--front" aria-label="Business card front">
    <div class="card__panel"></div>

    <div class="holder">
      <div class="holder__name">MARCUS LEE.</div>
      <div class="holder__role">Director</div>
    </div>

    <ul class="contact">
      <li>
        <svg viewBox="0 0 10 10" aria-hidden="true"><path d="M5 0.5a3.2 3.2 0 0 0-3.2 3.2C1.8 6 5 9.5 5 9.5S8.2 6 8.2 3.7A3.2 3.2 0 0 0 5 0.5z" fill="var(--brand-red)"/><circle cx="5" cy="3.7" r="1.2" fill="#fff"/></svg>
        <span>18 Tanjong Avenue<br>07-12 Tanjong Point<br>Singapore 438811</span>
      </li>
      <li>
        <svg viewBox="0 0 10 10" aria-hidden="true"><circle cx="5" cy="5" r="4.2" fill="none" stroke="var(--brand-red)" stroke-width="1.2"/><path d="M0.8 5h8.4M5 0.8c-2 2.4-2 6 0 8.4M5 0.8c2 2.4 2 6 0 8.4" fill="none" stroke="var(--brand-red)" stroke-width="0.8"/></svg>
        <span>http://www.ktplanora.com</span>
      </li>
      <li>
        <svg viewBox="0 0 10 10" aria-hidden="true"><rect x="0.6" y="2" width="8.8" height="6" fill="none" stroke="var(--brand-red)" stroke-width="1"/><path d="M0.6 2L5 5.6 9.4 2" fill="none" stroke="var(--brand-red)" stroke-width="1"/></svg>
        <span>marcus@ktplanora.com</span>
      </li>
    </ul>

    <div class="brand-box">
      <div class="brand-mark"></div>
      <div class="brand-name">KT Planora</div>
      <div class="brand-tagline">spaces delivered as promised</div>
    </div>

    <div class="card__band"></div>
  </section>

  <section class="card card--back" aria-label="Business card back">
    <div class="back-brand">
      <div class="brand-mark"></div>
      <div class="brand-name">KT Planora</div>
      <div class="brand-tagline">spaces delivered as promised</div>
    </div>
    <div class="card__band"></div>
  </section>

</body>
</html>
```